Bright Fern Custom Homes business card. Double sided. Modern. professional

Bright Fern Custom Homes
contemporary modern design with our logo /
Double sided with all our contact information
Use same Green colors as in our Logo. Contemporary logo that grabs your attention. Visually pleasing and balanced. Easy to read, and Vibrant. Would love an option for rounded edges. Embossed logo would be amazing.
Contact Information for Business Card
Dana Welk Owner / General Contractor Bright Fern Custom Homes p: 704.552.1830 m: 912.648.2071 e: brightferncustomhomes@mailbox.example w: www.brightferncustomhomes.example 218 Pryor Meadow Lane Batesburg, SC 29041

```html
<!DOCTYPE html>
<html lang="en">
<head>
<meta charset="utf-8">
<title>Bright Fern Custom Homes – Business Card</title>
<link href="https://fonts.googleapis.com/css2?family=Cinzel:wght@400&family=Cormorant+SC:wght@500&family=Montserrat:wght@500&display=swap" rel="stylesheet">
<style>
  :root {
    --green-deep: #4a7d00;
    --green-mid: #5ea00a;
    --green-bright: #7cc21e;
    --ink: #000000;
    --pattern: #161616;
    --paper: #ffffff;
  }
  * { margin: 0; padding: 0; box-sizing: border-box; }
  html, body { width: 1200px; height: 1200px; overflow: hidden; background: var(--paper); }
  .stage { position: relative; width: 1200px; height: 1200px; }

  .card { position: absolute; overflow: hidden; }

  /* Back side */
  .card-back {
    left: 58px; top: 47px; width: 831px; height: 539px;
    border-radius: 78px; background: var(--ink);
  }
  .back-pattern {
    position: absolute; left: 40px; top: 36px; width: 760px; height: 470px;
    background: radial-gradient(ellipse at 40% 45%, var(--pattern) 0%, #0c0c0c 55%, var(--ink) 100%);
  }
  .back-mark {
    position: absolute; left: 560px; top: 278px; width: 96px; height: 96px;
    border-radius: 50%;
    background: radial-gradient(circle at 65% 35%, var(--green-bright), var(--green-deep));
  }
  .back-wordmark {
    position: absolute; left: 430px; top: 416px; width: 376px;
    text-align: center;
  }
  .back-wordmark .brand-name {
    font-family: 'Cinzel', serif; font-weight: 400; font-size: 46px; line-height: 1;
    color: var(--green-mid); white-space: nowrap; letter-spacing: 0.05em;
  }
  .back-wordmark .brand-sub {
    margin-top: 24px;
    font-family: 'Montserrat', sans-serif; font-size: 11px;
    letter-spacing: 1.1em; color: var(--green-mid); white-space: nowrap;
  }

  /* Front side */
  .card-front {
    left: 324px; top: 627px; width: 833px; height: 543px;
    border-radius: 80px; background: var(--paper);
    border: 4px solid var(--ink);
  }
  .front-mark {
    position: absolute; left: 45px; top: 100px; width: 312px; height: 280px;
    display: flex; flex-direction: column; align-items: center; justify-content: center; gap: 16px;
  }
  .front-mark .mark-circle {
    width: 210px; height: 210px; border-radius: 50%; background: var(--green-deep);
  }
  .front-mark .mark-name {
    font-family: 'Cinzel', serif; font-weight: 400; font-size: 24px; color: var(--green-deep); white-space: nowrap;
  }

  .contact { position: absolute; left: 392px; top: 84px; width: 430px; }
  .person-name {
    font-family: 'Cinzel', serif; font-weight: 400; font-size: 33px; line-height: 1;
    color: var(--green-deep); letter-spacing: 0.08em; white-space: nowrap;
  }
  .person-role {
    margin-top: 11px; margin-left: 3px;
    font-family: 'Montserrat', sans-serif; font-size: 10.5px;
    letter-spacing: 0.22em; color: var(--green-mid); white-space: nowrap;
  }
  .rule { width: 255px; height: 1px; background: var(--green-deep); opacity: 0.8; }
  .rule-top { margin-top: 30px; }
  .address {
    margin: 24px 0 18px 4px;
    font-family: 'Cormorant SC', serif; font-size: 17px; line-height: 24px;
    letter-spacing: 0.1em; color: var(--green-deep);
  }
  .contact-list { list-style: none; margin-top: 26px; }
  .contact-list li {
    display: flex; align-items: center; height: 31px;
    font-family: 'Cinzel', serif; font-weight: 400; font-size: 14px; letter-spacing: 0.1em;
    color: var(--green-deep); white-space: nowrap; text-transform: uppercase;
  }
  .contact-list li.long { font-size: 12.5px; letter-spacing: 0.09em; }
  .contact-list svg { width: 18px; height: 18px; margin: 0 18px 0 2px; flex: none; }

  .front-band {
    position: absolute; left: 0; right: 0; bottom: 0; height: 77px;
    background: var(--green-deep); text-align: center; padding-top: 18px;
  }
  .front-band .brand-name {
    font-family: 'Cinzel', serif; font-weight: 400; font-size: 29px; line-height: 1;
    color: var(--paper); letter-spacing: 0.04em; white-space: nowrap;
  }
  .front-band .brand-sub {
    margin-top: 1px;
    font-family: 'Montserrat', sans-serif; font-size: 7px;
    letter-spacing: 1.1em; color: var(--paper); white-space: nowrap;
  }
</style>
</head>
<body>
<main class="stage">

  <section class="card card-back" aria-label="Card back">
    <div class="back-pattern" role="img" aria-label="Faint repeated brand pattern"></div>
    <div class="back-mark"></div>
    <div class="back-wordmark">
      <div class="brand-name">BRIGHT FERN</div>
      <div class="brand-sub">CUSTOM HOMES</div>
    </div>
  </section>

  <section class="card card-front" aria-label="Card front">
    <div class="front-mark">
      <div class="mark-circle"></div>
      <div class="mark-name">BRIGHT FERN</div>
    </div>

    <div class="contact">
      <h1 class="person-name">DANA WELK</h1>
      <p class="person-role">OWNER / GENERAL CONTRACTOR</p>
      <div class="rule rule-top"></div>
      <p class="address">218 Pryor Meadow Lane,<br>Cedar Hollow, NC 28041</p>
      <div class="rule"></div>
      <ul class="contact-list">
        <li>
          <svg viewBox="0 0 24 24" aria-hidden="true"><path d="M7 2 L10 7 L8 9 Q9 14 13 17 L15 15 L20 18 L18 22 Q5 20 4 5 Z" fill="none" stroke="var(--green-deep)" stroke-width="2"/></svg>
          704 552 1830
        </li>
        <li>
          <svg viewBox="0 0 24 24" aria-hidden="true"><rect x="6" y="2" width="12" height="20" rx="2" fill="none" stroke="var(--green-deep)" stroke-width="2"/><line x1="11" y1="19" x2="13" y2="19" stroke="var(--green-deep)" stroke-width="2"/></svg>
          912 648 2071
        </li>
        <li class="long">
          <svg viewBox="0 0 24 24" aria-hidden="true"><rect x="2" y="5" width="20" height="14" fill="var(--green-deep)"/><path d="M2 5 L12 13 L22 5 M2 19 L9 11 M22 19 L15 11" fill="none" stroke="#fff" stroke-width="1.5"/></svg>
          brightferncustomhomes@mailbox.example
        </li>
        <li class="long">
          <svg viewBox="0 0 24 24" aria-hidden="true"><circle cx="12" cy="12" r="9" fill="none" stroke="var(--green-deep)" stroke-width="2"/><path d="M3 12 H21 M12 3 Q6 12 12 21 M12 3 Q18 12 12 21" fill="none" stroke="var(--green-deep)" stroke-width="1.5"/></svg>
          www.brightferncustomhomes.example
        </li>
      </ul>
    </div>

    <div class="front-band">
      <div class="brand-name">BRIGHT FERN</div>
      <div class="brand-sub">CUSTOM HOMES</div>
    </div>
  </section>

</main>
</body>
</html>
```